Lumen Cove Skincare - Package Design

New Beauty label needing product packaging design. Looking for elegant and stylish design to represent our premium brand.

This project is for 1 label and 1 box design. The winning designer will be assigned another project for the next product in the range. (to be paid as a new project)

This product is for "Dead Sea Mud Mask". Please see the label format and jar attached. Please note there are 2 different jars we are considering (will have a mud inside). Please feel free to choose whichever one suits your design best.

The labels and boxes are to retain the product information, such as size, ingredients etc, but is to be updated to our brand. You can move or display the other information as you wish.

the size of the dead sea mud mask color box is 72*72*85mm (length*width*height)
the size of dead sea mud mask label is 218*58mm (width*height)

Target Market(s)

Women 15 to 65

Requirements
Must have
• Must be elegant and represent our brand which is a premium beauty product.
Should not have
• Dark blue. Dark purple etc. Colours should compliment the logo

```html
<!DOCTYPE html>
<html lang="en">
<head>
<meta charset="utf-8">
<title>Lumen Cove Skincare – Dead Sea Mud Mask Box</title>
<link href="https://fonts.googleapis.com/css2?family=Open+Sans:wght@400;600;700&display=swap" rel="stylesheet">
<style>
  :root {
    --page-bg: #f3f2f2;
    --panel: #cbc4c4;
    --panel-edge: #bdb5b5;
    --ink: #1c1a1a;
    --gold: #c9a23f;
    --white: #ffffff;
    --muted: #3a3636;
    --badge-pink: #b48a8a;
  }
  * { box-sizing: border-box; margin: 0; padding: 0; }
  html, body { width: 1200px; height: 1200px; overflow: hidden; }
  body {
    background: var(--page-bg);
    font-family: "Open Sans", Arial, sans-serif;
    color: var(--ink);
    position: relative;
  }
  .panel {
    position: absolute;
    background: var(--panel);
    border: 1px solid var(--panel-edge);
  }
  .panel-top   { left: 185px; top: 149px; width: 400px; height: 400px; }
  .panel-front { left: 185px; top: 579px; width: 400px; height: 472px; }
  .panel-side  { left: 615px; top: 579px; width: 400px; height: 472px; }

  .brand {
    position: absolute;
    left: 0;
    width: 100%;
    display: flex;
    flex-direction: column;
    align-items: center;
    gap: 10px;
  }
  .brand-dot { width: 16px; height: 16px; border-radius: 50%; background: var(--gold); }
  .brand-name { font-weight: 600; color: var(--gold); letter-spacing: 1px; white-space: nowrap; }

  .panel-top .brand { top: 160px; }
  .panel-top .brand-name { font-size: 24px; }

  .natural-badge {
    position: absolute;
    top: 18px; left: 18px;
    width: 48px; height: 60px;
    background: var(--white);
    text-align: center;
    padding-top: 12px;
  }
  .natural-badge .pct { display: block; font-size: 12px; font-weight: 600; color: var(--badge-pink); }
  .natural-badge .word { display: block; font-size: 7px; letter-spacing: 0.5px; margin-top: 2px; }

  .panel-front .brand { top: 80px; }
  .panel-front .brand-name { font-size: 21px; }

  .product-title {
    position: absolute;
    top: 195px; left: 0;
    width: 100%;
    text-align: center;
    line-height: 1.08;
  }
  .product-title .line-bold { display: block; font-size: 50px; font-weight: 700; }
  .product-title .line-light { display: block; font-size: 46px; font-weight: 400; }

  .benefits {
    position: absolute;
    top: 335px; left: 50%;
    transform: translateX(-50%);
    background: var(--white);
    display: flex;
    gap: 12px;
    padding: 4px 10px;
    font-size: 11px;
    white-space: nowrap;
  }
  .net-weight {
    position: absolute;
    top: 390px; width: 100%;
    text-align: center;
    font-size: 13px;
  }

  .recycle {
    position: absolute;
    top: 300px; left: 0;
    width: 100%;
    display: flex;
    flex-direction: column;
    align-items: center;
    gap: 5px;
  }
  .recycle-label { font-size: 9px; color: var(--muted); }
  .warning {
    position: absolute;
    top: 360px; width: 100%;
    text-align: center;
    font-size: 8px;
    line-height: 1.55;
    color: var(--muted);
    text-transform: uppercase;
  }
</style>
</head>
<body>
  <section class="panel panel-top">
    <div class="brand">
      <span class="brand-dot"></span>
      <span class="brand-name">Lumen Cove Skincare</span>
    </div>
  </section>

  <section class="panel panel-front">
    <div class="natural-badge"><span class="pct">100%</span><span class="word">NATURAL</span></div>
    <div class="brand">
      <span class="brand-dot"></span>
      <span class="brand-name">Lumen Cove Skincare</span>
    </div>
    <h1 class="product-title">
      <span class="line-bold">DEAD SEA</span>
      <span class="line-light">MUD MASK</span>
    </h1>
    <div class="benefits">
      <span>ANTI ACNE</span><span>DEEP SKIN CLEANRS</span><span>PRE REDUCER</span>
    </div>
    <p class="net-weight">250 g</p>
  </section>

  <section class="panel panel-side">
    <div class="recycle">
      <svg width="22" height="22" viewBox="0 0 26 26" aria-hidden="true">
        <circle cx="13" cy="13" r="12" fill="none" stroke="#3a3636" stroke-width="1.4"/>
        <path d="M9 16 L13 8 L17 16 Z" fill="none" stroke="#3a3636" stroke-width="1.4" stroke-linejoin="round"/>
      </svg>
      <span class="recycle-label">Recyclable Packaging</span>
    </div>
    <p class="warning">
      Warning<br>
      Burn within sight – keep away from children<br>
      Keep away from things that catch fire
    </p>
  </section>
</body>
</html>
```